Environmentally friendly Home and Office cleaning service needs a logo and web design!

Tidewell Housekeeping is a new startup looking for a logo and web design. We're base in Ottawa, Canada, and all of our products are eco-friendly, as well as being easy on the sensitivities of our clients.
We wash windows, walls, kitchens, bathrooms, dust, vacuum and wash floors on our hands and knees, and bring all of our own gear and supplies.
plumrake.example was my last website. It's functional, not bad - but just isn't great. I'm looking for a simple design, with few links or clickable buttons.
Colours I will leave to your creative mind to decide. I just want to see something that is relevant to "Tidewell Housekeeping."

Target Market(s)

Often it's women and gay men, ages 35-70
White collar government workers, usually with pets (cats, dogs)

Industry/Entity Type

Cleaning Service

Logo Text

Tidewell Housekeeping

Number of Pages Required

1 page

Font styles to use
Sans Serif

Colors

Designer to choose colors to be used in the design.

Requirements
Must have
• Colour, pictures

```html
<!DOCTYPE html>
<html lang="en">
<head>
<meta charset="utf-8">
<title>Tidewell Housekeeping</title>
<link href="https://fonts.googleapis.com/css2?family=Open+Sans:ital,wght@0,400;0,600;0,700;1,400&family=PT+Sans:wght@400;700&display=swap" rel="stylesheet">
<style>
:root{
  --green:#2f9a57;
  --green-band:#5ab46a;
  --green-deep:#3f8f50;
  --header-a:#33a05f;
  --header-b:#8fca58;
  --text:#3c3c3c;
  --muted:#666;
  --panel:#f3f3f3;
  --line:#d6d6d6;
  --footer:#0e1a2a;
  --white:#fff;
}
*{box-sizing:border-box;margin:0;padding:0}
html,body{width:1200px;height:3557px;overflow:hidden}
body{font-family:"Open Sans",Arial,sans-serif;color:var(--text);background:var(--white);position:relative}
.section{position:absolute;left:0;width:1200px}

/* header */
.site-header{top:0;height:104px;background:linear-gradient(90deg,var(--header-a),var(--header-b))}
.brand{position:absolute;left:133px;top:22px;display:flex;align-items:center;gap:10px}
.brand-dot{width:56px;height:56px;border-radius:50%;background:#e9f3c8}
.brand-name{font-family:"PT Sans",Arial,sans-serif;font-weight:700;font-size:28px;color:var(--white);line-height:1;white-space:nowrap}
.brand-tag{font-family:"Open Sans",Arial,sans-serif;font-style:italic;font-size:10.5px;color:var(--white);margin-top:5px;white-space:nowrap}
.main-nav{position:absolute;right:133px;top:42px;display:flex;gap:28px}
.main-nav a{color:var(--white);text-decoration:none;font-size:12px;font-weight:700;letter-spacing:.4px}
.main-nav a.active{border-bottom:2px solid var(--white);padding-bottom:3px}

/* hero */
.hero{top:104px;height:510px;background:linear-gradient(100deg,#b9c8cf 0%,#dfe6e4 35%,#c9b9a5 65%,#8a8278 100%)}
.hero-title{position:absolute;top:185px;width:100%;text-align:center;font-family:"PT Sans",Arial,sans-serif;font-weight:700;font-size:34px;color:var(--white)}
.call-btn{position:absolute;display:flex;align-items:center;height:46px;font-size:20px;text-decoration:none}
.call-btn .ico{width:46px;height:46px;display:flex;align-items:center;justify-content:center}
.call-btn .label{padding:0 22px}
.hero .call-btn{left:463px;top:245px;background:var(--green);color:var(--white)}
.hero .call-btn .ico{background:#24804a}
.slider-arrow{position:absolute;width:30px;height:30px;border-radius:50%;background:rgba(0,0,0,.35);display:flex;align-items:center;justify-content:center}
.hero .slider-arrow{top:228px}

/* intro */
.intro{top:614px;height:522px}
.h2{font-family:"PT Sans",Arial,sans-serif;font-weight:700;color:var(--green);text-align:center}
.intro .h2{position:absolute;top:72px;width:100%;font-size:32px}
.intro-copy{position:absolute;top:128px;left:160px;width:880px;text-align:center;font-size:12px;line-height:1.6}
.intro-copy .accent{color:var(--green);font-size:15px;line-height:1.5;margin:4px 0}
.rate-box{position:absolute;left:133px;top:295px;width:934px;height:142px;background:var(--panel);border:1px solid var(--line);text-align:center;padding-top:33px;font-size:25px;line-height:1.65}
.rate-box em{font-size:14px;color:var(--muted)}

/* how it works */
.how{top:1136px;height:1058px;background:var(--green-band);color:var(--white)}
.how-title{position:absolute;top:100px;width:100%;text-align:center;font-family:"PT Sans",Arial,sans-serif;font-weight:700;font-size:32px}
.how-sub{position:absolute;top:145px;width:100%;text-align:center;font-family:"PT Sans",Arial,sans-serif;font-weight:700;font-size:24px}
.card{position:absolute;top:216px;width:443px}
.card-photo{height:256px}
.card-body{height:256px;background:var(--green-deep);text-align:center;padding:38px 30px 0;font-size:14.5px;line-height:1.7}
.card-body svg{display:block;margin:0 auto 26px}
.how-copy{position:absolute;top:760px;left:133px;width:934px;text-align:center;font-size:15px;line-height:1.75}
.how-copy p+p{margin-top:14px}
.how .call-btn{left:465px;top:904px;width:273px;background:var(--white);color:var(--text)}
.how .call-btn .ico{background:#d8d8d8}

/* green cleaning */
.eco{top:2194px;height:740px}
.eco .h2{position:absolute;top:75px;width:100%;font-size:32px}
.eco-photo{position:absolute;top:131px;left:133px;width:934px;height:320px;background:linear-gradient(110deg,#c7b9a4 0%,#e2d7c6 40%,#d9d5cf 70%,#a7a29b 100%)}
.eco-list{position:absolute;top:472px;width:100%;text-align:center;list-style:none;font-size:17.5px;line-height:33px}
.outline-btn{position:absolute;top:614px;left:548px;width:104px;height:43px;border:1px solid #bdbdbd;border-radius:3px;display:flex;align-items:center;justify-content:center;font-size:12px;color:var(--text);text-decoration:none;background:var(--white)}

/* reviews */
.reviews{top:2934px;height:415px;background:var(--panel)}
.reviews .h2{position:absolute;top:78px;width:100%;font-size:31px}
.quote{position:absolute;top:130px;left:133px;width:934px;text-align:center;font-style:italic;font-size:12.5px;line-height:1.75;color:var(--muted)}
.reviewer{position:absolute;top:207px;width:100%;text-align:center;font-size:13px;color:var(--green)}
.avatar{position:absolute;top:237px;left:553px;width:94px;height:94px;border-radius:50%;background:radial-gradient(circle at 50% 45%,#e8d6cc,#b79c8c);border:3px solid var(--white)}
.plain-arrow{position:absolute;top:196px}

/* footer */
.site-footer{top:3349px;height:208px;background:var(--footer);color:#c9ced6;text-align:center}
.footer-nav{position:absolute;top:50px;width:100%;font-size:11.5px}
.footer-nav a{color:#c9ced6;text-decoration:none}
.footer-nav span{margin:0 8px}
.copyright{position:absolute;top:77px;width:100%;font-size:11.5px}
.social{position:absolute;top:112px;left:495px;display:flex;gap:16px}
.social span{width:41px;height:41px;border-radius:50%;border:1px solid #6b7585}
</style>
</head>
<body>

<header class="section site-header">
  <div class="brand">
    <div class="brand-dot"></div>
    <div>
      <div class="brand-name">Tidewell Housekeeping</div>
      <div class="brand-tag">"Let me be part of your team to keep your space clean"</div>
    </div>
  </div>
  <nav class="main-nav">
    <a class="active" href="#">HOME</a>
    <a href="#">ABOUT US</a>
    <a href="#">SERVICES</a>
    <a href="#">HOW IT WORKS</a>
    <a href="#">REVIEWS</a>
    <a href="#">CONTACT US</a>
  </nav>
</header>

<section class="section hero" role="img" aria-label="Smiling woman wiping a window with a blue cloth and yellow glove">
  <span class="slider-arrow" style="left:30px"><svg width="12" height="14" viewBox="0 0 12 14"><path d="M9 1 3 7l6 6" fill="none" stroke="#fff" stroke-width="2.5"/></svg></span>
  <span class="slider-arrow" style="right:30px"><svg width="12" height="14" viewBox="0 0 12 14"><path d="m3 1 6 6-6 6" fill="none" stroke="#fff" stroke-width="2.5"/></svg></span>
  <h1 class="hero-title">Vestibulum conadimentu</h1>
  <a class="call-btn" href="#">
    <span class="ico"><svg width="18" height="18" viewBox="0 0 24 24"><path fill="#fff" d="M6.6 10.8a15.1 15.1 0 0 0 6.6 6.6l2.2-2.2c.3-.3.7-.4 1-.2 1.1.4 2.3.6 3.6.6.6 0 1 .4 1 1V20c0 .6-.4 1-1 1A17 17 0 0 1 3 4c0-.6.4-1 1-1h3.5c.6 0 1 .4 1 1 0 1.3.2 2.5.6 3.6.1.3 0 .7-.2 1z"/></svg></span>
    <span class="label">Call : 613-555-0148</span>
  </a>
</section>

<section class="section intro">
  <h2 class="h2">Let us be part of your team to keep your space clean!</h2>
  <div class="intro-copy">
    <p>We will give your home the respect it deserves with careful attention to detail and thorough work. It can be a relief to know that you can leave and come back and never have to worry about dusting, vacuuming, windows or walls.</p>
    <p class="accent">We do all of that for you!</p>
    <p>You don't even have to think about providing any materials for us since we supply all of our own gear and equipment, all of which is 100% eco-friendly and kind on sensitivities.</p>
    <p class="accent">We are insured and have references available to confirm our work ethic and trustworthiness.</p>
  </div>
  <div class="rate-box">
    <p>Fees: 37.50/hour <em>(2.5 hour minimum)</em></p>
    <p>Phone: 613-555-0148 <em>(leave a message when you call)</em></p>
  </div>
</section>

<section class="section how">
  <h2 class="how-title">How It Works</h2>
  <p class="how-sub">The first clean is half-off because :</p>

  <div class="card" style="left:133px">
    <div class="card-photo" role="img" aria-label="Two cleaners in green uniforms tidying a living room" style="background:linear-gradient(120deg,#e6e2da,#cfc9bd 50%,#8a9a7e)"></div>
    <div class="card-body">
      <svg width="40" height="40" viewBox="0 0 40 40" fill="none" stroke="#fff" stroke-width="2"><path d="M26 8H9v26h17V24"/><circle cx="17" cy="18" r="5"/><path d="M17 15v3l2 1"/><path d="m22 28 12-12 3 3-12 12h-3z"/></svg>
      We don't give estimates. Houses can be very deceiving, and we don't want to set inappropriate expectations. The discounted rate gives us the ability to estimate just how long regular cleans will take.
    </div>
  </div>

  <div class="card" style="left:624px">
    <div class="card-photo" role="img" aria-label="Polished wooden floor reflecting tall glass windows" style="background:linear-gradient(180deg,#3d7fb8 0%,#6aa6d6 40%,#c48a4e 60%,#8a5124 100%)"></div>
    <div class="card-body">
      <svg width="40" height="40" viewBox="0 0 24 24"><path fill="#fff" d="m12 2 3 6.5 7 .8-5.2 4.8 1.4 7L12 17.6 5.8 21l1.4-7L2 9.3l7-.8z"/></svg>
      This also gives you the chance to test us out and see if we're a good fit.
    </div>
  </div>

  <div class="how-copy">
    <p>For the first clean, it'd be ideal if you were there so that we can go room to room and make sure everything is exactly as you like it to be. I don't want us leaving until you're happy!</p>
    <p>Assuming you like what you see, we can then schedule regular appointments. I will have a copy of your keys made and initial them so that no one knows who these keys belong to (Jane Doe would be "JD").</p>
  </div>
  <a class="call-btn" href="#">
    <span class="ico"><svg width="18" height="18" viewBox="0 0 24 24"><path fill="#555" d="M6.6 10.8a15.1 15.1 0 0 0 6.6 6.6l2.2-2.2c.3-.3.7-.4 1-.2 1.1.4 2.3.6 3.6.6.6 0 1 .4 1 1V20c0 .6-.4 1-1 1A17 17 0 0 1 3 4c0-.6.4-1 1-1h3.5c.6 0 1 .4 1 1 0 1.3.2 2.5.6 3.6.1.3 0 .7-.2 1z"/></svg></span>
    <span class="label">Call : 613-555-0148</span>
  </a>
</section>

<section class="section eco">
  <h2 class="h2">What makes green cleaning environmentally friendly?</h2>
  <div class="eco-photo" role="img" aria-label="Gloved hands spraying and wiping a wooden table"></div>
  <ul class="eco-list">
    <li>We use unscented, non-toxic, chemical-free cleaners</li>
    <li>We use vinegar as an antiseptic and deodorizer when needed, as well as for windows and mirrors</li>
    <li>We use baking soda if we need more aggressive scrubbing</li>
    <li>We use a HEPA-filter vacuum for allergen relief</li>
  </ul>
  <a class="outline-btn" href="#">Learn More</a>
</section>

<section class="section reviews">
  <h2 class="h2">Reviews</h2>
  <svg class="plain-arrow" style="left:48px" width="14" height="24" viewBox="0 0 14 24"><path d="M12 2 2 12l10 10" fill="none" stroke="#999" stroke-width="2"/></svg>
  <svg class="plain-arrow" style="right:48px" width="14" height="24" viewBox="0 0 14 24"><path d="m2 2 10 10L2 22" fill="none" stroke="#999" stroke-width="2"/></svg>
  <p class="quote">" Etiam quis aliquet risus. Duis ornare erat eget magna dapibus, in accumsan quam pharetra. Nam tempus, quam in bibendum vulputate, sapien dolor viverra nisi, vitae euismod elit turpis et nulla. Aliquam erat volutpat. Pellentesque blandit lacus eget nunc faucibus, et tincidunt eros viverra. Phasellus consequat sagittis nisi suscipit feugiat. Cras eget leo sed nunc hendrerit ultricies eu at nisl. "</p>
  <p class="reviewer">Maren Holt, City</p>
  <div class="avatar" role="img" aria-label="Reviewer portrait"></div>
</section>

<footer class="section site-footer">
  <div class="footer-nav">
    <a href="#">Home</a><span>|</span><a href="#">About Us</a><span>|</span><a href="#">Services</a><span>|</span><a href="#">How It Works</a><span>|</span><a href="#">Reviews</a><span>|</span><a href="#">Contact Us</a>
  </div>
  <p class="copyright">Copyright © 2017 Tidewell Housekeeping. All rights reserved.</p>
  <div class="social" aria-label="Social links">
    <span></span><span></span><span></span><span></span>
  </div>
</footer>

</body>
</html>
```